Professional business cards for real estate development company

I need business cards for my new real estate development company. The company, "KORVA" is a real estate development, investment, and advisory firm with a focus on multifamily, office, and mixed-use projects across primary and secondary markets in the Southeast United States.

Style preference is modern

Industry/Entity Type

Real Estate Development

Contact Information for Business Card

The business cards need to include:
Name
Title
Mailing Address
Phone Number
Web Address

Logo is attached. I would like white to be the primary color with incorporation of the company colors: #232D3A and #B5A451

Font styles to use
Other font styles liked:
• Montserrat, Avenir

Requirements
Must have
• Company Logo. No need to include the company name since the name is in the logo.
Should not have
• No line type designs

```html
<!DOCTYPE html>
<html lang="en">
<head>
<meta charset="utf-8">
<title>KORVA Development – Business Cards</title>
<link href="https://fonts.googleapis.com/css2?family=Montserrat:wght@400;500;700&display=swap" rel="stylesheet">
<style>
  :root {
    --navy: #232D3A;
    --gold: #B5A451;
    --white: #FFFFFF;
    --ink: #2A323D;
    --backdrop: #3A3438;
  }
  * { box-sizing: border-box; margin: 0; padding: 0; }
  html, body {
    width: 1200px; height: 912px; overflow: hidden;
    background: var(--backdrop);
    font-family: "Montserrat", sans-serif;
  }
  .canvas { position: relative; width: 1200px; height: 912px; }

  .card {
    position: absolute;
    width: 560px; height: 320px;
    border-radius: 16px;
    overflow: hidden;
    box-shadow: 0 14px 30px rgba(0,0,0,0.45);
  }

  /* Front */
  .card-front { left: 60px; top: 80px; background: var(--navy); }
  .card-front .brand {
    position: absolute; inset: 0;
    display: flex; align-items: center; justify-content: center;
  }
  .brand-name {
    font-weight: 500;
    color: var(--white);
    letter-spacing: 6px;
    font-size: 40px;
    text-transform: uppercase;
    line-height: 1;
  }
  .brand-name small {
    display: block;
    font-size: 14px;
    letter-spacing: 9px;
    margin-top: 10px;
    text-align: center;
  }

  /* Back */
  .card-back { left: 580px; top: 500px; background: var(--white); }
  .card-back .brand {
    position: absolute; right: 40px; top: 30px;
  }
  .card-back .brand-name { color: var(--navy); font-size: 30px; letter-spacing: 5px; }
  .card-back .brand-name small { font-size: 10px; letter-spacing: 7px; margin-top: 8px; }

  .rule-long {
    position: absolute; left: 200px; right: 30px; top: 118px;
    height: 1px; background: var(--gold);
  }
  .holder { position: absolute; left: 36px; top: 140px; }
  .holder-name {
    font-weight: 700; font-size: 20px; color: var(--navy);
    text-transform: uppercase; letter-spacing: 0.5px;
  }
  .holder-name .surname { color: var(--gold); }
  .holder-title { font-size: 13px; color: var(--ink); margin-top: 2px; }
  .rule-short { width: 150px; height: 1px; background: var(--gold); margin: 9px 0 8px; }
  .contacts { list-style: none; font-size: 12.5px; color: var(--ink); }
  .contacts li { display: flex; align-items: center; gap: 8px; line-height: 17px; }
  .contacts svg { width: 10px; height: 10px; fill: var(--navy); flex: none; }
  .contacts .accent { color: var(--gold); }

  .address {
    position: absolute; right: 30px; top: 190px;
    text-align: right; font-size: 12px; color: var(--ink); line-height: 16px;
  }
  .footer-wave { position: absolute; left: 0; bottom: 0; width: 560px; height: 100px; }
</style>
</head>
<body>
<main class="canvas">
  <section class="card card-front" aria-label="Card front">
    <div class="brand">
      <p class="brand-name">KORVA<small>Development</small></p>
    </div>
  </section>

  <section class="card card-back" aria-label="Card back">
    <div class="brand">
      <p class="brand-name">KORVA<small>Development</small></p>
    </div>
    <div class="rule-long"></div>

    <div class="holder">
      <p class="holder-name">Dorian <span class="surname">Vale</span></p>
      <p class="holder-title">Managing Director</p>
      <div class="rule-short"></div>
      <ul class="contacts">
        <li><svg viewBox="0 0 10 10"><path d="M2 0.5 L3.6 2.6 L2.6 3.6 C3.2 5 5 6.8 6.4 7.4 L7.4 6.4 L9.5 8 L8.2 9.5 C4.5 9.2 0.8 5.5 0.5 1.8 Z"/></svg>(123)555-0148</li>
        <li><svg viewBox="0 0 10 10"><path d="M2.5 0 H7.5 V10 H2.5 Z M3.3 1 V8 H6.7 V1 Z"/></svg>(987)555-0162</li>
        <li><svg viewBox="0 0 10 10"><path d="M0 2 H10 V8.5 H0 Z M0.6 2.4 L5 5.8 L9.4 2.4"/></svg>info@korvadeveloper.com</li>
        <li><svg viewBox="0 0 10 10"><circle cx="5" cy="5" r="4.8"/></svg><span>www.<span class="accent">korvadeveloper</span>.com</span></li>
      </ul>
    </div>

    <p class="address">48 Rue Lamar, 3rd Floor B<br>Marrakesh - Morocco</p>

    <svg class="footer-wave" viewBox="0 0 560 100" preserveAspectRatio="none" aria-hidden="true">
      <path d="M0 100 L0 86 C180 86 320 80 370 46 C400 24 420 12 470 10 L560 10 L560 100 Z" fill="var(--navy)"/>
      <path d="M0 78 C170 76 310 70 362 42" fill="none" stroke="var(--gold)" stroke-width="4" stroke-linecap="round"/>
    </svg>
  </section>
</main>
</body>
</html>
```